International Medical travel company needs professional card

We just purchased a logo through sketch nest, and now need a business card. We contract with Middle Eastern governments to bring patients who need complex medical care to the U.S. for treatment. We will upload logo. Titles, names, contact info, etc. needs to be in English on one side, Arabic on the other

Target Market(s)

Health administrators, professionals

Industry/Entity Type

Health Care

Contact Information for Business Card

logo on each side. Usual name/title/contact info

Font styles to use
Serif
Sans Serif

Colors
0255a3

Requirements
Must have
• English one side, Arabic the other

```html
<!DOCTYPE html>
<html lang="en">
<head>
<meta charset="utf-8">
<title>Meridian Care — Business Cards</title>
<link rel="stylesheet" href="https://fonts.googleapis.com/css2?family=Tinos:wght@400;700&family=Questrial&family=Noto+Naskh+Arabic:wght@400;700&display=swap">
<style>
  :root {
    --bg: #2b2b2b;
    --card-black: #050505;
    --brand-blue: #0255a3;
    --panel-blue: #1d6cb6;
    --arabic-blue: #2a72c4;
    --gold: #c8b53c;
    --yellow: #e6dc3a;
    --white: #ffffff;
  }
  * { margin: 0; padding: 0; box-sizing: border-box; }
  html, body { width: 1200px; height: 900px; overflow: hidden; }
  body { background: var(--bg); position: relative; font-family: "Questrial", sans-serif; }

  .card {
    position: absolute;
    width: 620px; height: 354px;
    background: var(--card-black);
    box-shadow: 0 18px 40px rgba(0,0,0,.55);
    overflow: hidden;
  }

  .icon { width: 12px; height: 12px; flex: none; }

  /* Shared brand block: plain square above the stacked name */
  .brand-block {
    position: absolute; top: 0; height: 100%;
    display: flex; flex-direction: column; align-items: center; justify-content: center; gap: 16px;
  }
  .brand-block .square { width: 40px; height: 40px; border: 4px solid var(--gold); }
  .brand-name {
    font-family: "Questrial", sans-serif; color: var(--gold);
    font-size: 40px; text-align: center; line-height: 1.05; letter-spacing: 1px;
  }

  /* Arabic side */
  .card--arabic { left: 110px; top: 80px; }
  .card--arabic .brand-block { right: 20px; width: 260px; }
  .card--arabic .contact {
    position: absolute; right: 290px; top: 88px; width: 260px;
    direction: rtl; text-align: right; color: var(--white);
  }
  .card--arabic .person-name {
    font-family: "Noto Naskh Arabic", serif; font-weight: 700;
    font-size: 30px; color: var(--arabic-blue); line-height: 1.2;
  }
  .card--arabic .person-title {
    font-family: "Noto Naskh Arabic", serif; font-weight: 700; font-size: 17px;
    color: var(--yellow); line-height: 1.4;
  }
  .card--arabic .address {
    font-family: "Noto Naskh Arabic", serif; font-size: 15px; line-height: 1.6; margin-bottom: 4px;
  }
  .card--arabic .lines { direction: ltr; font-size: 16px; line-height: 1.45; }
  .card--arabic .lines li { list-style: none; display: flex; justify-content: flex-end; align-items: center; gap: 10px; }

  /* English side */
  .card--english { left: 470px; top: 470px; }
  .card--english .brand-block { left: 0; width: 270px; }
  .info-panel { position: absolute; left: 270px; top: 0; width: 350px; height: 100%; }
  .info-panel svg.panel-shape { position: absolute; inset: 0; }
  .info-panel .contact { position: absolute; left: 44px; top: 70px; color: var(--white); }
  .info-panel .person-name { font-family: "Tinos", serif; font-weight: 700; font-size: 24px; }
  .info-panel .person-title { color: var(--yellow); font-size: 16px; margin-bottom: 6px; }
  .info-panel .address { font-size: 16px; line-height: 1.3; margin-bottom: 10px; }
  .info-panel .lines li { list-style: none; font-size: 16px; line-height: 1.35; display: flex; align-items: center; gap: 10px; }
</style>
</head>
<body>

  <!-- Arabic side -->
  <section class="card card--arabic" aria-label="Business card, Arabic side">
    <div class="contact">
      <p class="person-name">كريم حداد</p>
      <p class="person-title">مدير</p>
      <p class="address">طريق النخيل، 21577<br>جدة، المملكة العربية السعودية</p>
      <ul class="lines">
        <li>+330 5128 -4406
          <svg class="icon" viewBox="0 0 12 12"><path d="M2 1l2.5 0 1 3-1.5 1c.7 1.4 1.6 2.3 3 3l1-1.5 3 1V11C6 11 1 6 1 2z" fill="var(--gold)"/></svg></li>
        <li>info@meridiancare.com
          <svg class="icon" viewBox="0 0 12 12"><rect x="1" y="2.5" width="10" height="7" fill="none" stroke="var(--gold)" stroke-width="1.3"/><path d="M1 2.5l5 4 5-4" fill="none" stroke="var(--gold)" stroke-width="1.3"/></svg></li>
        <li>www.meridiancare.com
          <svg class="icon" viewBox="0 0 12 12"><circle cx="6" cy="6" r="5" fill="none" stroke="var(--gold)" stroke-width="1.2"/><ellipse cx="6" cy="6" rx="2.2" ry="5" fill="none" stroke="var(--gold)" stroke-width="1"/><path d="M1 6h10" stroke="var(--gold)" stroke-width="1"/></svg></li>
      </ul>
    </div>
    <div class="brand-block">
      <span class="square"></span>
      <p class="brand-name">MERIDIAN<br>CARE</p>
    </div>
  </section>

  <!-- English side -->
  <section class="card card--english" aria-label="Business card, English side">
    <div class="brand-block">
      <span class="square"></span>
      <p class="brand-name">MERIDIAN<br>CARE</p>
    </div>
    <div class="info-panel">
      <svg class="panel-shape" viewBox="0 0 350 354" preserveAspectRatio="none">
        <path d="M0 0H350V354H0V120L10 110L0 100Z" fill="var(--panel-blue)"/>
        <rect x="60" y="40" width="230" height="230" fill="none" stroke="rgba(255,255,255,.08)" stroke-width="8"/>
      </svg>
      <div class="contact">
        <p class="person-name">Karim Haddad</p>
        <p class="person-title">Director</p>
        <p class="address">Palm Avenue, 21577<br>Jeddah, Saudi Arabia</p>
        <ul class="lines">
          <li><svg class="icon" viewBox="0 0 12 12"><path d="M2 1l2.5 0 1 3-1.5 1c.7 1.4 1.6 2.3 3 3l1-1.5 3 1V11C6 11 1 6 1 2z" fill="var(--gold)"/></svg>+330 5128 -4406</li>
          <li><svg class="icon" viewBox="0 0 12 12"><rect x="1" y="2.5" width="10" height="7" fill="none" stroke="var(--gold)" stroke-width="1.3"/><path d="M1 2.5l5 4 5-4" fill="none" stroke="var(--gold)" stroke-width="1.3"/></svg>info@meridiancare.com</li>
          <li><svg class="icon" viewBox="0 0 12 12"><circle cx="6" cy="6" r="5" fill="none" stroke="var(--gold)" stroke-width="1.2"/><ellipse cx="6" cy="6" rx="2.2" ry="5" fill="none" stroke="var(--gold)" stroke-width="1"/><path d="M1 6h10" stroke="var(--gold)" stroke-width="1"/></svg>www.meridiancare.com</li>
        </ul>
      </div>
    </div>
  </section>

</body>
</html>
```